Trucking Insurance Website Design

We are working with a Trucking Insurance company in California. They provide vehicle insurance for trucking companies and truckers.
As you might imagine, there are no websites we could find for inspiration for trucking insurance. But below are sites that do similar insurance.
https://brindlemorecover.com/trucking-insurance/
https://www.haulwardpolicy.com/california-commercial-truck-insurance
Thank you for taking the time to consider designing a website for us. We are web developers based in Stockton, CA, USA. Most of our projects go through the same process. Understanding this process may help you win a project with us. We custom-code all of our websites in-house. We don’t have any requirements as to what tools you use for your design, but we ask that you follow these guidelines.
IMAGES:
If you use any images or icons in the design, we ask that you have a link to the asset so we can purchase the image/icon. Most of the designs we submit do not have the customer’s images on them unless they have some great images. Be creative; show us the feeling you are trying to portray with your image choices. Use any royalty-free site you choose. We subscribe to Quillen and mainly use their images, but we can purchase images outside of Quillen. PLEASE NOTE: we will not submit designs to clients with watermarks on the images.
FONTS:
We ask that you identify the fonts you’re using in the design. This can be done in a message if you want. We typically use Marlowe Type and Quillen Type.
CONTENT:
We're always open to different content and ideas. We often submit designs with stock images so the client can see our vision. We typically take pictures after the website launch to use their images with our vision. Lorem Ipsum is fine for paragraphs, but we ask that you make the Headers with correct English. We want to be able to show the vision and identify the sections of the website.
INSPIRATION:
We typically add a couple of links in the brief of websites we like to help you get started in your design.
REVISIONS:
We do not often ask for revisions of the designs unless we see something in the design that may not appeal to the client. If there are slight changes that we want to make, we do that in the development process.
FEEDBACK:
We rarely give feedback on designs during the design process. We are working on many website projects and do not have the time to provide feedback. We usually respond if your request is well thought out and asks specific questions, but a note asking “feedback, please” usually goes unanswered.
1 page

```html
<!DOCTYPE html>
<html lang="en">
<head>
<meta charset="utf-8">
<title>Ridgeline Insurance – Trucking Insurance</title>
<link rel="stylesheet" href="https://fonts.googleapis.com/css2?family=Montserrat:wght@400;600;700;800&family=Mulish:wght@400;500;600;700&display=swap">
<style>
:root{
  --blue:#4a5fbe;
  --blue-title:#5468c4;
  --blue-soft:#b9c3e4;
  --section-bg:#ecf0f8;
  --red:#c4161c;
  --red-dark:#7a1418;
  --ink:#1f2230;
  --text:#3a3d48;
  --outline:#8a8fa3;
  --footer:#202127;
  --footer-text:#e6e8f0;
  --white:#ffffff;
}
*{margin:0;padding:0;box-sizing:border-box}
html,body{width:1200px;height:2323px;overflow:hidden;background:var(--white)}
body{position:relative;font-family:'Mulish',sans-serif;color:var(--text)}
.abs{position:absolute}

/* header */
.brand{left:114px;top:30px;display:flex;align-items:center;gap:10px}
.brand-dot{width:34px;height:34px;border-radius:50%;background:var(--blue)}
.brand-name{font-family:'Mulish',sans-serif;font-weight:700;font-size:17px;letter-spacing:2px;color:var(--ink);line-height:1.2}
.top-contact{top:12px;display:flex;align-items:center;gap:10px;font-size:15px;color:var(--ink)}
.top-contact b{font-weight:600}
.icon-circle{width:40px;height:40px;border-radius:50%;background:var(--blue);display:flex;align-items:center;justify-content:center}
.top-sep{left:811px;top:24px;width:1px;height:12px;background:var(--blue)}
.nav{left:469px;top:64px;width:731px;height:47px;background:linear-gradient(90deg,#7a7f93 0%,#5d6cb8 45%,var(--blue) 100%);clip-path:polygon(22px 0,100% 0,100% 100%,0 100%,10px 20px);display:flex;align-items:center;padding-left:40px;gap:32px}
.nav a{color:var(--white);text-decoration:none;font-size:15px}

/* hero */
.hero{left:0;top:110px;width:1200px;height:500px;background:linear-gradient(100deg,#2a3140 0%,#6b5a55 22%,#e79a4a 32%,#8f2a3a 50%,#b8283f 70%,#9aa4b0 100%)}
.hero-shape{left:0;top:490px}
.hero-kicker{left:114px;top:226px;color:var(--white);font-size:24px;font-weight:500}
.hero-kicker::after{content:"";display:block;width:66px;height:2px;background:var(--white);margin-top:8px}
.hero-title{left:112px;top:286px;font-family:'Montserrat',sans-serif;font-size:54px;line-height:58px;font-weight:800;color:var(--white)}
.hero-title .outline{font-weight:400;color:transparent;-webkit-text-stroke:2px var(--white);display:block}
.scroll-mouse{left:113px;top:446px}

/* about */
.about-photo{left:111px;top:657px;width:362px;height:362px;border-radius:50%;background:linear-gradient(135deg,#9fc0e4,#2d3fb0 55%,#6c6f80);z-index:2}
.about-ring{left:137px;top:657px;width:362px;height:362px;border-radius:50%;background:#5164b5}
.section-title{font-family:'Montserrat',sans-serif;font-weight:800;color:var(--blue-title);font-size:41px;letter-spacing:.5px}
.section-title .outline{font-weight:500;color:transparent;-webkit-text-stroke:1.3px var(--outline);margin-left:10px}
.about-title{left:571px;top:676px}
.about-text{left:568px;top:746px;width:520px;font-size:14.6px;line-height:28px}
.about-text p+p{margin-top:4px}
.btn{left:572px;top:945px;width:116px;height:44px;background:var(--red);color:var(--white);font-size:15px;display:flex;align-items:center;justify-content:center}

/* industry */
.industry{left:0;top:1069px;width:1200px;height:511px;background:var(--section-bg)}
.industry-title{left:0;top:1128px;width:1200px;text-align:center}
.card{top:1215px;width:296px;height:309px;background:var(--white);border-radius:0 0 14px 14px;text-align:center;padding-top:43px}
.card svg{display:block;margin:0 auto}
.card h3{font-size:17px;font-weight:600;color:var(--ink);margin-top:28px}
.card p{font-size:14.6px;line-height:30px;margin:14px auto 0;width:250px}

/* experts */
.experts-title{left:0;top:1637px;width:1200px;text-align:center}
.experts-text{left:112px;top:1733px;width:520px;font-size:14.6px;line-height:28px}
.experts-panel{left:693px;top:1727px;width:507px;height:153px;background:var(--blue-soft);border-radius:52px 0 0 52px}
.panel-row{left:44px;display:flex;align-items:center;gap:14px;font-size:25px;color:var(--ink)}
.panel-row b{font-weight:600}
.dark-circle{width:41px;height:41px;border-radius:50%;background:radial-gradient(circle at 35% 30%,#c6262c,var(--red-dark) 70%,#3a0b0d);display:flex;align-items:center;justify-content:center}

/* footer */
.footer-shape{left:0;top:1930px}
.footer{left:0;top:2030px;width:1200px;height:293px;background:var(--footer)}
.footer-brand{left:112px;top:2135px;display:flex;align-items:center;gap:12px}
.footer-brand .brand-dot{background:var(--white);width:40px;height:40px}
.footer-brand .brand-name{color:var(--white);font-size:22px;letter-spacing:3px}
.footer h4,.footer-col h4{font-family:'Mulish',sans-serif;font-weight:500;font-size:19px;color:var(--footer-text)}
.footer-col{color:var(--footer-text);font-size:15px}
.footer-col ul{list-style:none;margin-top:18px;margin-left:6px}
.footer-col li{line-height:30px}
.fc-item{display:flex;gap:14px;align-items:flex-start;line-height:30px}
.copyright{left:0;top:2281px;width:1250px;text-align:center;font-size:15px;color:#a9acb8}
</style>
</head>
<body>

<!-- Header -->
<div class="abs brand"><span class="brand-dot"></span><span class="brand-name">RIDGELINE<br>INSURANCE</span></div>

<div class="abs top-contact" style="left:568px">
  <span class="icon-circle"><svg width="18" height="18" viewBox="0 0 24 24"><path fill="#fff" d="M6.6 10.8a15.1 15.1 0 0 0 6.6 6.6l2.2-2.2a1 1 0 0 1 1-.25 11.4 11.4 0 0 0 3.6.57 1 1 0 0 1 1 1V20a1 1 0 0 1-1 1A17 17 0 0 1 3 4a1 1 0 0 1 1-1h3.5a1 1 0 0 1 1 1c0 1.25.2 2.45.57 3.57a1 1 0 0 1-.25 1z"/></svg></span>
  <span>Call: <b>+1-800-555-0142</b></span>
</div>
<div class="abs top-sep"></div>
<div class="abs top-contact" style="left:845px">
  <span class="icon-circle"><svg width="18" height="14" viewBox="0 0 24 18"><path fill="#fff" d="M2 0h20a2 2 0 0 1 2 2v1L12 10 0 3V2a2 2 0 0 1 2-2zM0 5.3l12 7 12-7V16a2 2 0 0 1-2 2H2a2 2 0 0 1-2-2z"/></svg></span>
  <span>Email: <b>info@ridgelinecover.com</b></span>
</div>

<nav class="abs nav">
  <a href="#">Home</a><a href="#">About</a><a href="#">Trucking</a><a href="#">Personal</a><a href="#">Business</a><a href="#">Benefits</a><a href="#">Contact</a>
</nav>

<!-- Hero -->
<div class="abs hero" role="img" aria-label="Red semi truck driving on a highway at sunset"></div>
<svg class="abs hero-shape" width="1200" height="130" viewBox="0 0 1200 130">
  <path fill="#fff" d="M0 37 Q600 145 1200 37 L1200 130 L0 130Z"/>
  <path fill="var(--red)" d="M207 73 Q600 150 987 73 Q600 136 207 73Z"/>
</svg>
<div class="abs hero-kicker">WELCOME TO</div>
<div class="abs hero-title">RIDGELINE<span class="outline">INSURANCE</span></div>
<svg class="abs scroll-mouse" width="26" height="34" viewBox="0 0 26 34" aria-hidden="true">
  <rect x="1.5" y="1.5" width="23" height="31" rx="11.5" fill="none" stroke="#fff" stroke-width="2"/>
  <path d="M13 8v13M9 17l4 4 4-4" fill="none" stroke="#fff" stroke-width="2"/>
</svg>

<!-- About -->
<div class="abs about-ring"></div>
<div class="abs about-photo" role="img" aria-label="Truck driver standing beside a blue semi truck"></div>
<h2 class="abs section-title about-title">ABOUT<span class="outline">US</span></h2>
<div class="abs about-text">
  <p>Lorem ipsum dolor sit amet, consectetur adipiscing elit, sed do eiusmod tempor incididunt ut labore et dolore magnliqua. Quis ipsum suspendisse ultrices gravida. Risus commodo viverra maecenasaccu lacus vel facilisis.</p>
  <p>Lorem ipsum dolor sit amet, consectetur adipiscing elit, sed do eiusmod tempor incididunt ut labore et dolore magnliqua. Quis ipsum suspendisse ultrices gravida. Risus commodo viverra maecenasaccu.</p>
</div>
<a class="abs btn">Learn More</a>

<!-- Industry -->
<div class="abs industry"></div>
<h2 class="abs section-title industry-title">INDUSTRY<span class="outline">SPECIALIZATION</span></h2>

<div class="abs card" style="left:114px">
  <svg width="72" height="72" viewBox="0 0 72 72" fill="none" stroke-width="2.4">
    <circle cx="30" cy="32" r="12" stroke="var(--blue)"/>
    <path stroke="var(--blue)" d="M30 8v7M30 49v7M6 32h7M47 32h7M13 15l5 5M42 44l5 5M13 49l5-5M42 20l5-5"/>
    <path stroke="var(--red)" d="M50 36 68 68H32z"/>
    <path stroke="var(--red)" d="M50 48v10M50 62v2"/>
  </svg>
  <h3>RISK MANAGEMENT</h3>
  <p>Sed ut perspiciati unde omnis iste natus sit voluptatem accusantium doloremque laudantium, totam.</p>
</div>

<div class="abs card" style="left:453px">
  <svg width="72" height="72" viewBox="0 0 72 72" fill="none" stroke-width="2.4">
    <path stroke="var(--red)" d="M19 2 34 8v12c0 10-7 16-15 19C11 36 4 30 4 20V8z"/>
    <path stroke="var(--red)" d="M12 20l5 5 9-9"/>
    <path stroke="var(--blue)" d="M36 24h20l10 12v20H6V42M56 24v32M56 36h10"/>
    <circle cx="18" cy="60" r="5" stroke="var(--blue)" fill="#fff"/>
    <circle cx="54" cy="60" r="5" stroke="var(--blue)" fill="#fff"/>
  </svg>
  <h3>PRODUCTS</h3>
  <p>Sed ut perspiciati unde omnis iste natus sit voluptatem accusantium doloremque laudantium, totam.</p>
</div>

<div class="abs card" style="left:793px">
  <svg width="72" height="72" viewBox="0 0 72 72" fill="none" stroke-width="2.4">
    <path stroke="var(--blue)" d="M36 4v10M18 12l7 8M54 12l-7 8M6 34h10M56 34h10"/>
    <circle cx="36" cy="3" r="2.5" stroke="var(--blue)"/>
    <circle cx="16" cy="10" r="3" stroke="var(--blue)"/>
    <circle cx="56" cy="10" r="3" stroke="var(--blue)"/>
    <circle cx="5" cy="34" r="3" stroke="var(--blue)"/>
    <circle cx="67" cy="34" r="3" stroke="var(--blue)"/>
    <path stroke="var(--red)" d="M24 34a12 12 0 0 1 24 0"/>
    <path stroke="var(--red)" d="M32 68V34a4 4 0 0 1 8 0v12l10 2v20M40 46v-4M30 50l-4-4a3 3 0 0 0-4 4l8 10"/>
  </svg>
  <h3>OPTIONS</h3>
  <p>Sed ut perspiciati unde omnis iste natus sit voluptatem accusantium doloremque laudantium, totam.</p>
</div>

<!-- Experts -->
<h2 class="abs section-title experts-title">EXPERTS<span class="outline">AVAILABLE</span></h2>
<p class="abs experts-text">Nemo enim ipsam voluptatem quia voluptas sit aspernatur aut odit aut fugit, sed quia consequuntur magni doleos qui ratione voluptatem sequi nesciunt. Neque ro quisquam est, qui dolorem ipsum quia dolor sit amet, consectetur, adipisci velit,.</p>
<div class="abs experts-panel">
  <div class="abs panel-row" style="top:24px">
    <span class="dark-circle"><svg width="18" height="18" viewBox="0 0 24 24"><path fill="#fff" d="M6.6 10.8a15.1 15.1 0 0 0 6.6 6.6l2.2-2.2a1 1 0 0 1 1-.25 11.4 11.4 0 0 0 3.6.57 1 1 0 0 1 1 1V20a1 1 0 0 1-1 1A17 17 0 0 1 3 4a1 1 0 0 1 1-1h3.5a1 1 0 0 1 1 1c0 1.25.2 2.45.57 3.57a1 1 0 0 1-.25 1z"/></svg></span>
    <span>Call: +1-800-555-0142</span>
  </div>
  <div class="abs panel-row" style="top:82px">
    <span class="dark-circle"><svg width="18" height="14" viewBox="0 0 24 18"><path fill="#fff" d="M2 0h20a2 2 0 0 1 2 2v1L12 10 0 3V2a2 2 0 0 1 2-2zM0 5.3l12 7 12-7V16a2 2 0 0 1-2 2H2a2 2 0 0 1-2-2z"/></svg></span>
    <span>Email: <b>info@ridgelinecover.com</b></span>
  </div>
</div>

<!-- Footer -->
<svg class="abs footer-shape" width="1200" height="110" viewBox="0 0 1200 110">
  <path fill="var(--footer)" d="M0 94 Q600 -20 1200 94 L1200 110 L0 110Z"/>
  <path fill="var(--red)" d="M170 66 Q600 -30 1035 66 Q600 -8 170 66Z"/>
</svg>
<footer class="abs footer"></footer>

<div class="abs footer-brand"><span class="brand-dot"></span><span class="brand-name">RIDGELINE<br>INSURANCE</span></div>

<div class="abs footer-col" style="left:451px;top:2053px">
  <h4>Contact us</h4>
  <div style="margin-top:18px">
    <div class="fc-item">
      <svg width="18" height="22" viewBox="0 0 18 24" style="margin-top:5px"><path fill="var(--blue)" d="M9 0a9 9 0 0 1 9 9c0 6-9 15-9 15S0 15 0 9a9 9 0 0 1 9-9zm0 5a4 4 0 1 0 0 8 4 4 0 0 0 0-8z"/></svg>
      <span>Ridgeline Insurance,<br>Address comes here</span>
    </div>
    <div class="fc-item" style="margin-top:15px">
      <svg width="18" height="18" viewBox="0 0 24 24" style="margin-top:5px"><path fill="var(--blue)" d="M6.6 10.8a15.1 15.1 0 0 0 6.6 6.6l2.2-2.2a1 1 0 0 1 1-.25 11.4 11.4 0 0 0 3.6.57 1 1 0 0 1 1 1V20a1 1 0 0 1-1 1A17 17 0 0 1 3 4a1 1 0 0 1 1-1h3.5a1 1 0 0 1 1 1c0 1.25.2 2.45.57 3.57a1 1 0 0 1-.25 1z"/></svg>
      <span>+1-800-555-0142</span>
    </div>
    <div class="fc-item" style="margin-top:16px">
      <svg width="18" height="14" viewBox="0 0 24 18" style="margin-top:9px"><path fill="var(--blue)" d="M2 0h20a2 2 0 0 1 2 2v1L12 10 0 3V2a2 2 0 0 1 2-2zM0 5.3l12 7 12-7V16a2 2 0 0 1-2 2H2a2 2 0 0 1-2-2z"/></svg>
      <span>hello@ridgelinecover.com</span>
    </div>
  </div>
</div>

<div class="abs footer-col" style="left:746px;top:2053px">
  <h4>Quick Links</h4>
  <ul><li>Home</li><li>About</li><li>Trucking</li><li>Personal</li><li>Business</li></ul>
</div>

<div class="abs footer-col" style="left:935px;top:2053px">
  <h4>Other Links</h4>
  <ul><li>Tearms &amp; Conditions</li><li>Privacy Policy</li><li>Benefite</li><li>Contact Us</li></ul>
</div>

<div class="abs copyright">2023 Ridgeline Insurance. All Rights Reserved.</div>

</body>
</html>
```